I own a small business whose primary function is Professional Fashion and Commercial Photography and has a secondary function of Talent Management of Models/Actors. I've used PrintaNova in the past to print my own design, but I'd like something a bit more topical, fresh and done by an artist instead of a photographer (me).

My company logo is included with a few selected horizontal (landscape) photos of some of my models--I'd like to use a single model photo as the background for the entire card, either in color or converted to black and white, at opacity enough to see the photo but not too much to obscure any text or the company logo, or use a photo as a share of the card (not the entire background), or use all the three models on the card in some manor... Our company colors are white, black, grey-silver and red.

Industry/Entity Type

Small Business

Contact Information for Business Card

Darnell Voskuijl, Owner
KLT Studios
PO Box 7316
Millbrook VT 05999-7316
(555) 014-2273
dan@kltstudios-example,.com

```html
<!DOCTYPE html>
<html lang="en">
<head>
<meta charset="utf-8">
<title>KLT Studios – Business Card</title>
<link href="https://fonts.googleapis.com/css2?family=Open+Sans:wght@400;600&display=swap" rel="stylesheet">
<style>
  :root{
    --bg:#e9e7e3;
    --paper:#ffffff;
    --paper-shade:#ececec;
    --ink:#2b2b2b;
    --ink-soft:#5a5a5a;
    --silver:#9a9a9a;
    --red:#d7172f;
    --black:#070707;
    --black-soft:#2a2a2a;
  }
  *{box-sizing:border-box;margin:0;padding:0}
  html,body{width:1200px;height:1023px;overflow:hidden}
  body{background:var(--bg);font-family:"Open Sans",Arial,sans-serif;position:relative}
  .card{position:absolute;left:220px;width:760px;height:434px;overflow:hidden;
        box-shadow:0 10px 30px rgba(0,0,0,.25)}
  /* Front */
  .card--front{top:50px;background:linear-gradient(135deg,var(--paper) 0%,var(--paper) 60%,var(--paper-shade) 100%)}
  .front__photo{position:absolute;left:0;top:250px;width:300px;height:184px;
        background:linear-gradient(160deg,#c9d3db 0%,#7a8a99 45%,#3c4652 100%)}
  .front__brand{position:absolute;left:40px;top:36px;display:flex;align-items:center;gap:14px}
  .brand-square{width:30px;height:30px;background:var(--red)}
  .front__brand .brand-name{font-size:40px;font-weight:600;color:var(--ink);letter-spacing:1px}
  .front__rule{position:absolute;left:40px;right:40px;top:100px;height:2px;background:var(--red)}
  .front__person{position:absolute;left:320px;top:140px}
  .person-name{font-size:26px;font-weight:600;color:var(--ink);letter-spacing:.5px;text-transform:uppercase}
  .person-title{font-size:16px;color:var(--ink-soft);margin-top:2px}
  .front__divider{position:absolute;left:320px;top:232px;width:270px;height:1px;background:var(--ink)}
  .contact-list{position:absolute;left:320px;top:250px;list-style:none}
  .contact-list li{display:flex;align-items:center;gap:10px;font-size:16px;color:var(--ink-soft);margin-bottom:8px}
  .contact-list svg{width:16px;height:16px;flex:none}
  .front__vrule{position:absolute;left:608px;top:120px;width:1px;height:240px;background:var(--ink-soft)}
  .front__address{position:absolute;left:626px;top:140px;font-size:15px;line-height:1.5;color:var(--ink-soft)}
  .front__address .company{color:var(--red);font-weight:600}
  /* Back */
  .card--back{top:530px;background:linear-gradient(160deg,var(--black-soft) 0%,var(--black) 45%,var(--black) 100%)}
  .back__brand{position:absolute;left:50px;top:60px;display:flex;align-items:center;gap:14px}
  .back__brand .brand-name{font-size:40px;font-weight:600;color:#ffffff;letter-spacing:1px}
  .back__rule{position:absolute;left:50px;top:124px;width:330px;height:2px;background:var(--red)}
  .back__photo{position:absolute;left:330px;top:150px;width:430px;height:284px}
</style>
</head>
<body>
  <section class="card card--front">
    <div class="front__photo" role="img" aria-label="Photograph of a model in a patterned shirt"></div>
    <div class="front__brand"><span class="brand-square"></span><span class="brand-name">KLT Studios</span></div>
    <div class="front__rule"></div>
    <div class="front__person">
      <p class="person-name">Darnell Voskuijl</p>
      <p class="person-title">General Director</p>
    </div>
    <div class="front__divider"></div>
    <ul class="contact-list">
      <li><svg viewBox="0 0 16 16"><rect width="16" height="16" rx="2" fill="#d7172f"/><rect x="5" y="3" width="6" height="10" rx="1" fill="#fff"/></svg>(555) 014-2273</li>
      <li><svg viewBox="0 0 16 16"><rect width="16" height="16" rx="2" fill="#d7172f"/><rect x="3" y="5" width="10" height="7" fill="#fff"/><path d="M3 5l5 4 5-4" stroke="#d7172f" fill="none"/></svg>dan@kltstudios-example.com</li>
      <li><svg viewBox="0 0 16 16"><rect width="16" height="16" rx="2" fill="#d7172f"/><circle cx="8" cy="8" r="4.5" fill="none" stroke="#fff"/><path d="M3.5 8h9M8 3.5v9" stroke="#fff"/></svg>www.kltstudios-example.com</li>
    </ul>
    <div class="front__vrule"></div>
    <address class="front__address">
      <span class="company">KLT Studios</span><br>
      PO Box 7316 Millbrook<br>
      VT 05999-7316
    </address>
  </section>

  <section class="card card--back">
    <div class="back__brand"><span class="brand-square"></span><span class="brand-name">KLT Studios</span></div>
    <div class="back__rule"></div>
    <svg class="back__photo" viewBox="0 0 430 284" role="img" aria-label="Black and white portrait of a model framed by nested squares">
      <defs>
        <linearGradient id="photoTone" x1="0" y1="0" x2="1" y2="1">
          <stop offset="0" stop-color="#8c8c8c"/>
          <stop offset="1" stop-color="#2e2e2e"/>
        </linearGradient>
      </defs>
      <rect x="60" y="40" width="370" height="244" fill="url(#photoTone)"/>
      <rect x="20" y="10" width="400" height="300" fill="none" stroke="#bdbdbd" stroke-opacity=".5" stroke-width="16"/>
      <rect x="70" y="55" width="340" height="260" fill="none" stroke="#d0d0d0" stroke-opacity=".45" stroke-width="12"/>
      <rect x="120" y="100" width="280" height="220" fill="none" stroke="#e0e0e0" stroke-opacity=".4" stroke-width="8"/>
    </svg>
  </section>
</body>
</html>
```